Clear Plastic Card Design

I am looking to have a business card designed from my logo icon. I am looking to match the style of a different business card I have attached in the files.
Looking for a card that is plastic, with layers of transparency in the shape of my logo icon (also attached in the files) - not a circle like the other card. The winning design will incorporate the red icon logo on the front and back and include the charity's name, "Lanterns for the Weary" in the same or similar font, as well as an email and phone number. For now, use the email: email@lanternsfortheweary.org and the phone number 555-318-4072.
We like how the sample business card has transparency, partial and full opacity layers and a matching color scheme. Files will need to be in vector so that our business card printing company can work with it.
UPDATE:
We've some excellent designs in, thank you everyone! I got an early review from the owner, and he requested a minor redirect to find his perfect design. He wants the design to stand out by NOT being a rectangle. Try instead a circle, square, or best yet - something that falls in the outline of the logo icon, either fully or partially. Thank you, everyone!
Contact Information for Business Card
Lanterns for the Weary text should be incorporated as well as a phone and email.
Look and feel

```html
<!DOCTYPE html>
<html lang="en">
<head>
<meta charset="utf-8">
<title>Lanterns for the Weary – Clear Card</title>
<link rel="stylesheet" href="https://fonts.googleapis.com/css2?family=Questrial&display=swap">
<style>
  :root {
    --backdrop: #1c1c1e;
    --clear-plastic: rgba(150, 150, 150, 0.42);
    --brand-red: #d7141f;
    --deep-red: #c00014;
    --brand-orange: #f05a00;
    --ember: #e8361a;
    --paper: #ffffff;
    --ink: #111111;
    --contact-text: #ffe9e3;
  }
  html, body {
    margin: 0;
    padding: 0;
    width: 1200px;
    height: 792px;
    overflow: hidden;
    background: var(--backdrop);
  }
  .card-spread {
    display: block;
    width: 1200px;
    height: 792px;
  }
  .brand-text {
    font-family: "Questrial", sans-serif;
  }
  .contact-line {
    font-family: "Questrial", sans-serif;
    font-size: 12.5px;
    fill: var(--contact-text);
  }
  .contact-icon {
    fill: none;
    stroke: var(--brand-orange);
    stroke-width: 1.6;
  }
</style>
</head>
<body>
<svg class="card-spread" viewBox="0 0 1515 1000" xmlns="http://www.w3.org/2000/svg">

  <!-- Back of card: contact side -->
  <g class="card card-back">
    <path class="clear-body" fill="var(--clear-plastic)"
          d="M119,637 L119,362 Q119,307 174,307 L735,307 L735,470 Q735,637 575,637 Z"/>
    <path class="layer-orange" fill="var(--brand-orange)"
          d="M119,637 L119,430 Q160,322 290,307 L530,307 Q475,485 305,637 Z"/>
    <path class="layer-ember" fill="var(--ember)"
          d="M119,637 L119,455 Q165,335 330,307 L522,307 Q465,485 298,637 Z"/>
    <path class="layer-red" fill="var(--brand-red)"
          d="M119,637 L119,480 Q180,345 375,307 L516,307 Q460,482 292,637 Z"/>

    <text class="brand-text brand-watermark" fill="#ea4a2c" font-size="44">
      <tspan x="190" y="440">Lanterns</tspan>
      <tspan x="190" y="492">for the</tspan>
      <tspan x="190" y="544">Weary</tspan>
    </text>

    <path class="contact-leaf" fill="var(--deep-red)"
          d="M380,598 Q380,480 470,402 Q560,346 680,347 Q713,347 712,380 Q700,500 590,580 Q530,626 420,627 Q380,627 380,598 Z"/>

    <g class="contact-details" transform="translate(452,548) rotate(-44)">
      <text class="contact-line" x="14" y="0">email@lanternsfortheweary.org</text>
      <text class="contact-line" x="14" y="20">555-318-4072</text>
      <text class="contact-line" x="14" y="40">www.lanternsfortheweary.org</text>
    </g>
    <g class="contact-icons">
      <rect class="contact-icon" x="442" y="550" width="11" height="8" transform="rotate(-44 447 554)"/>
      <path class="contact-icon" d="M458,566 q-2,8 6,8 l3,-3"/>
      <circle class="contact-icon" cx="480" cy="583" r="5.5"/>
      <path class="contact-icon" d="M474.5,583 h11 M480,577.5 v11"/>
    </g>
  </g>

  <!-- Front of card: name side -->
  <g class="card card-front">
    <path class="clear-body" fill="var(--clear-plastic)"
          d="M780,307 L1342,307 Q1397,307 1397,362 L1397,637 L955,637 Q780,637 780,470 Z"/>
    <path class="layer-red" fill="var(--deep-red)"
          d="M985,307 L1397,307 L1397,637 L1212,637 Q1060,490 985,307 Z"/>
    <path class="layer-orange" fill="var(--brand-orange)"
          d="M998,307 L1250,307 Q1390,340 1397,470 L1397,637 L1225,637 Q1075,490 998,307 Z"/>
    <path class="layer-ember" fill="var(--ember)"
          d="M998,307 L1215,307 Q1370,345 1388,480 L1397,637 L1225,637 Q1075,490 998,307 Z"/>
    <path class="layer-paper" fill="var(--paper)"
          d="M998,307 L1160,307 Q1380,335 1397,540 L1397,637 L1222,637 Q1078,490 998,307 Z"/>

    <path class="front-leaf" fill="var(--brand-orange)"
          d="M805,372 Q802,347 836,347 Q960,345 1050,410 Q1136,480 1137,598 Q1137,627 1106,627 L992,627 Q880,600 830,482 Q806,424 805,372 Z"/>

    <g class="front-brand" transform="translate(1112,388) rotate(45)">
      <text class="brand-text" fill="var(--ink)" font-size="25">
        <tspan x="0" y="0">Lanterns for the</tspan>
        <tspan x="0" y="26">Weary</tspan>
      </text>
      <circle class="brand-dot" cx="96" cy="18" r="11" fill="var(--brand-red)"/>
    </g>
  </g>
</svg>
</body>
</html>
```